Real Estate Virtual Company Needs Eye Catching Flyer for Convention- ASAP

We need an 8 1/2 x 11 flyer to show potential clients what we do. We would like to have it double sided. The back should have a description of our major services. With the front, we need some creativity. We'd like to have our logo and we'd like to have something visual that gives the message of what we do. We give buyers a tour of homes for sale using photos, video and 3D tours, as if they were there but they can be anywhere using a computer, tablet or mobile device. The front should also have the tagline " Your 24/7 Open House Starts Here." If that's not possible design something modern and eye catching with our logo as the centerpiece. Note: Voxelwright and PlanLoop are two services that we offer. The logos are attached. They do not have to be included. We are including them here in case you feel you can use them. Our "DwellScopeLive" is the most important. We are uploading a previous flyer to show what we use. The back has a description of each service. We'd like use the the text and descriptions of this flyer but add the starting pricet o the services on the back. HDR Photos "Starting at $129" Walk-Through Video "Starting at $229" PlanLoop Interactive Floor Plans ''Starting at $209" Voxelwright 3D "Starting at $269" Add-Ons: Replace Drone with "Aerial Photos & Video" (Where available) Add "Virtual Twilight" Add "Agent Promo Videos" Add "Brevix Business Tours" Remove "Pondra Walk-Through Tours" Remove "Narration for Video Tours"
Real Estate Agents
Designer to choose colors to be used in the design.

```html
<!DOCTYPE html>
<html lang="en">
<head>
<meta charset="utf-8">
<title>DwellScopeLive Flyer</title>
<link href="https://fonts.googleapis.com/css2?family=Cabin:wght@400;500;600&display=swap" rel="stylesheet">
<style>
  :root {
    --ink: #3a3a3c;
    --lime: #cfd93c;
    --mist: #e4e5e6;
    --frame: #9b9b93;
    --text: #2b2b2b;
    --paper: #ffffff;
  }
  * { box-sizing: border-box; margin: 0; padding: 0; }
  html, body { width: 1200px; height: 898px; overflow: hidden; background: var(--paper); }
  body { position: relative; font-family: "Cabin", "Gill Sans", sans-serif; color: var(--text); }

  .page { position: absolute; width: 490px; height: 634px; background: var(--paper); outline: 1px solid #ececec; overflow: hidden; }
  .page--front { left: 83px; top: 139px; }
  .page--back { left: 625px; top: 140px; }
  .page svg.art { position: absolute; left: 0; top: 0; width: 490px; height: 634px; }
  .abs { position: absolute; }

  /* front */
  .tagline { left: 285px; width: 196px; top: 95px; text-align: center; color: #fff; font-size: 27px; line-height: 34px; font-weight: 400; }
  .tagline em { font-style: italic; color: var(--lime); }
  .brand-name { left: 285px; width: 196px; top: 430px; text-align: center; color: var(--ink); font-size: 21px; font-weight: 600; }
  .front-services { right: 38px; top: 521px; text-align: right; color: #fff; font-size: 12px; line-height: 21px; list-style: none; }
  .contact { left: 25px; top: 556px; font-size: 11px; line-height: 20px; color: #444; font-style: normal; }

  /* back */
  .services-title { right: 29px; top: 36px; font-size: 25px; font-weight: 600; color: #111; }
  .price { font-size: 7.5px; line-height: 10px; color: #333; }
  .price strong { display: block; font-size: 12px; line-height: 14px; font-weight: 500; letter-spacing: .3px; }
  .price--right { text-align: right; }
  .service-card { position: absolute; border: 2px solid var(--frame); background: var(--paper); padding: 14px 16px 0 16px; }
  .service-card h3 { font-size: 13px; font-weight: 500; color: #1e1e1e; margin-bottom: 8px; white-space: nowrap; }
  .service-card p { font-size: 9.2px; line-height: 14.3px; color: #222; }
  .partner { position: absolute; right: 14px; bottom: 8px; font-size: 12px; font-weight: 600; color: var(--ink); }
  .addons-title { right: 32px; top: 456px; font-size: 16px; font-weight: 500; color: #333; }
  .addons { right: 30px; top: 499px; text-align: right; color: #fff; font-size: 11px; line-height: 18.3px; list-style: none; }
</style>
</head>
<body>

<section class="page page--front">
  <svg class="art" viewBox="0 0 490 634">
    <defs>
      <linearGradient id="hall" x1="0" y1="0" x2="1" y2="1">
        <stop offset="0" stop-color="#3e5a7e"/><stop offset=".55" stop-color="#d9d6cf"/><stop offset="1" stop-color="#9a6a43"/>
      </linearGradient>
      <linearGradient id="living" x1="0" y1="0" x2="1" y2="1">
        <stop offset="0" stop-color="#c8ccd0"/><stop offset=".5" stop-color="#a9a39a"/><stop offset="1" stop-color="#b0774a"/>
      </linearGradient>
      <linearGradient id="family" x1="0" y1="0" x2="1" y2="1">
        <stop offset="0" stop-color="#d6d3cc"/><stop offset=".5" stop-color="#ece9e3"/><stop offset="1" stop-color="#a87b52"/>
      </linearGradient>
    </defs>
    <rect x="0" y="533" width="490" height="101" fill="var(--mist)"/>
    <rect x="17" y="0" width="16" height="125" fill="var(--mist)"/>
    <rect x="39" y="0" width="78" height="125" fill="var(--mist)"/>
    <rect x="240" y="0" width="40" height="125" fill="var(--mist)"/>
    <polygon points="123,0 233,0 233,128 123,185" fill="var(--lime)"/>
    <g fill="none" stroke="#222" stroke-width="1.6" stroke-linejoin="round">
      <rect x="139" y="42" width="28" height="20" rx="1"/>
      <line x1="135" y1="67" x2="171" y2="67"/>
      <rect x="161" y="52" width="10" height="18" rx="1"/>
      <rect x="188" y="50" width="32" height="20" rx="2"/>
      <rect x="194" y="46" width="8" height="4"/>
      <circle cx="204" cy="60" r="6"/>
      <circle cx="204" cy="60" r="3"/>
      <polyline points="139,101 156,86 173,101"/>
      <polyline points="143,98 143,119 169,119 169,98"/>
      <path d="M149 109 a9 9 0 0 1 14 0 M152 113 a5 5 0 0 1 8 0"/>
      <circle cx="156" cy="116" r="1"/>
      <circle cx="196" cy="91" r="5"/>
      <circle cx="208" cy="91" r="5"/>
      <rect x="189" y="97" width="24" height="13" rx="1"/>
      <polygon points="213,100 221,96 221,111 213,107"/>
      <polyline points="195,121 201,110 207,121"/>
    </g>
    <circle cx="252" cy="158" r="25" fill="#fff" stroke="var(--lime)" stroke-width="2"/>
    <g fill="none" stroke="#333" stroke-width="1.3">
      <path d="M258 146 a12 12 0 1 0 -14 21"/>
      <polyline points="255,143 259,147 262,142"/>
      <polyline points="243,154 247,158 253,151"/>
    </g>
    <text x="250" y="170" font-family="Cabin, sans-serif" font-size="12" fill="#333">24</text>
    <polygon points="285,0 481,0 481,238 383,356 285,238" fill="var(--ink)"/>
    <polygon points="0,165 141,232 141,380 0,313" fill="url(#hall)" role="img" aria-label="Photo of an entry hall with a curving staircase and blue walls"/>
    <polygon points="153,150 296,221 296,366 153,299" fill="url(#living)" role="img" aria-label="Photo of a living room with a stone fireplace and large wall clock"/>
    <polygon points="71,345 296,451 296,611 71,501" fill="url(#family)" role="img" aria-label="Photo of a bright family room with fireplace, sofa and coffee table"/>
    <polygon points="237,504 473,504 473,615 313,615" fill="var(--ink)"/>
  </svg>

  <h1 class="abs tagline">Your <em>24/7</em><br>Open House<br>Starts Here</h1>
  <div class="abs brand-name">DwellScopeLive</div>
  <ul class="abs front-services">
    <li>HDR Photos</li>
    <li>Interactive Floor Plans</li>
    <li>Walk-Through Video Tours</li>
    <li>3D Tours</li>
  </ul>
  <address class="abs contact">
    www.DwellScopeLive.com<br>
    855-DSL-VIEW (855-375-8439)<br>
    info@dwellscopelive.com
  </address>
</section>

<section class="page page--back">
  <svg class="art" viewBox="0 0 490 634">
    <defs>
      <linearGradient id="house" x1="0" y1="0" x2="0" y2="1">
        <stop offset="0" stop-color="#6f9fd3"/><stop offset=".45" stop-color="#8c9a88"/><stop offset="1" stop-color="#6f8f4a"/>
      </linearGradient>
      <linearGradient id="pool" x1="0" y1="0" x2="0" y2="1">
        <stop offset="0" stop-color="#7aa6d8"/><stop offset=".55" stop-color="#9a9d8e"/><stop offset="1" stop-color="#3fb1c9"/>
      </linearGradient>
      <linearGradient id="aerial" x1="0" y1="0" x2="0" y2="1">
        <stop offset="0" stop-color="#4c6b34"/><stop offset=".6" stop-color="#6f8a48"/><stop offset="1" stop-color="#8a7a52"/>
      </linearGradient>
    </defs>
    <polygon points="99,53 208,2 208,133 99,133" fill="url(#house)" role="img" aria-label="Photo of a two-storey colonial home with stone front"/>
    <polygon points="218,2 327,57 327,133 218,133" fill="url(#pool)" role="img" aria-label="Photo of the back of a large home with swimming pool"/>
    <rect x="360" y="68" width="107" height="3" fill="var(--lime)"/>
    <polygon points="87,457 165,457 87,527" fill="var(--lime)"/>
    <polygon points="0,605 87,529 87,605" fill="#3d4447"/>
    <polygon points="228,482 490,482 490,610 315,610" fill="var(--ink)"/>
    <polygon points="191,477 321,634 48,634" fill="url(#aerial)" role="img" aria-label="Aerial photo of an estate home with pool surrounded by trees"/>
  </svg>

  <h2 class="abs services-title">Services</h2>

  <div class="abs price" style="left:28px; top:105px">Starting at<strong>$129</strong></div>
  <div class="abs price price--right" style="right:30px; top:106px">Starting at<strong>$229</strong></div>
  <div class="abs price" style="left:198px; top:287px">Starting at<strong>$209</strong></div>
  <div class="abs price price--right" style="right:30px; top:290px">Starting at<strong>$269</strong></div>

  <article class="service-card" style="left:20px; top:135px; width:155px; height:144px">
    <h3>HDR Photos</h3>
    <p>Your listing deserve the best. Our Hi-Res Multiple Exposure Photos are sure to make any listing stand out. Guaranteed Blue Skies for all exterior photos. Next Day Delivery.</p>
  </article>

  <article class="service-card" style="left:201px; top:137px; width:267px; height:136px">
    <h3>Walk-Through Video Home Tours</h3>
    <p>Get more listings and sell them faster with our affordable Walk-Through Video Home Tours. Each Video HomeTour includes HDR Photos, Walk-through Video, Property Websites, and Streamora Syndication. More exposure means more eyes on your listings and more leads for you.</p>
  </article>

  <article class="service-card" style="left:16px; top:317px; width:232px; height:138px">
    <h3>PlanLoop Interactive Floor Plans</h3>
    <p>Our Floor Plan Home Tours are a complete, immersive listing solution that offers users an incredible understanding and perception of space with Precision Floor Plans and a 360, 3D Virtual Tour.</p>
    <span class="partner">PlanLoop</span>
  </article>

  <article class="service-card" style="left:258px; top:319px; width:210px; height:118px">
    <h3>Voxelwright 3D HomeTours</h3>
    <p>An all-in-one reality capture system that gives you realistic, interactive 3D and VR experiences that feel as real as being there.</p>
    <span class="partner">Voxelwright</span>
  </article>

  <h3 class="abs addons-title">Add-ons:</h3>
  <ul class="abs addons">
    <li>Aerial Photos &amp; Video (where available)</li>
    <li>Virtual Staging</li>
    <li>Virtual Twilight</li>
    <li>Agent Promo Videos</li>
    <li>Brevix Business Tours</li>
  </ul>
</section>

</body>
</html>
```